Painting Contractor Business Card Design

We are looking for a cool, bold, modern, polished, business card design. We are a high-end residential painting contractor. Please incorporate our logo and keep with our green/black color scheme. We are interested in seeing 2-sided and 1-sided options. Thank you very much!

Industry/Entity Type

Business

Contact Information for Business Card

Info for the card:
Owen Talsky
mobile 206-555-0193
email owen@kestrowfinish.net
web www.kestrowfinish.net

```html
<!DOCTYPE html>
<html lang="en">
<head>
<meta charset="utf-8">
<title>Kestrow Finish — Business Card</title>
<link rel="stylesheet" href="https://fonts.googleapis.com/css2?family=Mulish:wght@400;600;800&display=swap">
<style>
  :root {
    --backdrop: #8e8e90;
    --card: #ffffff;
    --ink: #1b1b1b;
    --green: #3bb54a;
  }
  html, body {
    margin: 0;
    padding: 0;
    width: 1200px;
    height: 910px;
    overflow: hidden;
    background: var(--backdrop);
    font-family: "Mulish", "Century Gothic", sans-serif;
  }
  .card {
    position: absolute;
    left: 100px;
    top: 169px;
    width: 1000px;
    height: 572px;
    background: var(--card);
    box-shadow: 0 6px 24px rgba(0,0,0,0.25);
    overflow: hidden;
  }
  .card__band {
    position: absolute;
    inset: 0;
  }
  .card__content {
    position: absolute;
    left: 0;
    top: 0;
    width: 860px;
    height: 100%;
    text-align: center;
    color: var(--ink);
  }
  .brand {
    position: absolute;
    top: 48px;
    left: 0;
    width: 100%;
    display: flex;
    align-items: center;
    justify-content: center;
    gap: 18px;
  }
  .brand__square {
    width: 52px;
    height: 52px;
    background: var(--green);
  }
  .brand__name {
    font-weight: 800;
    font-size: 46px;
    letter-spacing: 3px;
    color: var(--ink);
    text-transform: uppercase;
  }
  .person {
    position: absolute;
    top: 160px;
    left: 0;
    width: 100%;
  }
  .person__name {
    margin: 0;
    font-weight: 800;
    font-size: 86px;
    line-height: 1;
  }
  .person__line {
    margin: 14px 0 0;
    font-weight: 400;
    font-size: 40px;
    line-height: 1.15;
  }
  .website {
    position: absolute;
    left: 0;
    width: 100%;
    bottom: 56px;
    margin: 0;
    font-weight: 600;
    font-size: 66px;
  }
</style>
</head>
<body>
  <div class="card">
    <svg class="card__band" width="1000" height="572" viewBox="0 0 1000 572" aria-hidden="true">
      <path d="M860 0 H1000 V572 H935 Q900 300 860 0 Z" fill="var(--green)"/>
    </svg>
    <div class="card__content">
      <div class="brand">
        <span class="brand__square"></span>
        <span class="brand__name">Kestrow Finish</span>
      </div>
      <div class="person">
        <h1 class="person__name">Owen Talsky</h1>
        <p class="person__line">Mobile 206-555-0193</p>
        <p class="person__line">owen@kestrowfinish.net</p>
      </div>
      <p class="website">www.kestrowfinish.net</p>
    </div>
  </div>
</body>
</html>
```